We need a refreshed business card. Our company is a venture capital investment firm focused on investing in medical devices. Logo is attached. please also see our website www.velmoracapital.example

Target Market(s)

investors and potential investment targets

Industry/Entity Type

medical investments

Contact Information for Business Card

logo, name, title, email, phone, website, address,

Colors
0054AA
0677BA
7BADD7
CADEEF
E8F1F8
0094D4
00A9DD
6FCCEA
C7EBF8
E9F6FB
00AB8E
00BBA5
67D7C9
C6EFE9
E9F9F6

Requirements
Must have
• fresh modern design
Nice to have
• QR code leading to our linked in page, short description of what we do “Early Stage Medical Device Investors”

```html
<!DOCTYPE html>
<html lang="en">
<head>
<meta charset="utf-8">
<title>Velmora Business Card</title>
<link href="https://fonts.googleapis.com/css2?family=Open+Sans:wght@400;600&display=swap" rel="stylesheet">
<style>
  :root {
    --page-bg: #e9ecef;
    --card-white: #ffffff;
    --brand-blue: #0054AA;
    --brand-teal: #00AB8E;
    --slate: #474c58;
    --slate-line: #e6e8ec;
    --back-blue: #1878c8;
    --silver: #d9dee4;
    --text-dark: #2c2f36;
  }
  * { box-sizing: border-box; margin: 0; padding: 0; }
  html, body { width: 1200px; height: 873px; overflow: hidden; }
  body {
    background: var(--page-bg);
    font-family: "Open Sans", sans-serif;
    display: flex;
    align-items: center;
    justify-content: center;
    gap: 60px;
  }
  .card {
    width: 520px;
    height: 297px;
    position: relative;
    overflow: hidden;
    box-shadow: 0 6px 18px rgba(0,0,0,0.18);
  }

  /* Front */
  .card-front { background: var(--card-white); }
  .front-header {
    position: absolute; left: 0; top: 0; width: 100%; height: 172px;
  }
  .brand-lockup {
    position: absolute; left: 28px; top: 56px;
    display: flex; align-items: center; gap: 12px;
  }
  .brand-mark {
    display: flex; align-items: center; gap: 7px;
    color: var(--brand-blue);
    font-weight: 600; font-size: 28px; letter-spacing: 0.3px;
  }
  .brand-mark .dot {
    width: 10px; height: 10px; border-radius: 50%; background: var(--brand-teal);
  }
  .brand-divider { width: 1px; height: 56px; background: var(--text-dark); }
  .brand-name {
    font-size: 10px; line-height: 1.25; letter-spacing: 1.1px;
    color: var(--text-dark); text-transform: uppercase;
  }
  .front-photo {
    position: absolute; left: 300px; top: 0; width: 220px; height: 172px;
    background: linear-gradient(180deg, #cfe0f2 0%, #a9c7e4 40%, #7d9aa8 62%, #6f8a5a 80%, #8c7a62 100%);
  }
  .front-band {
    position: absolute; left: 0; top: 172px; width: 100%; height: 125px;
    background: var(--slate);
    border-top: 3px double var(--slate-line);
    color: #ffffff;
  }
  .person { position: absolute; left: 28px; top: 22px; }
  .person-name { font-size: 19px; font-weight: 400; }
  .person-title { font-size: 10px; color: #c9ccd2; margin-top: 2px; }
  .contact-list {
    position: absolute; left: 300px; top: 18px;
    list-style: none; font-size: 11px; line-height: 1.6;
  }
  .contact-list li { display: flex; align-items: flex-start; gap: 7px; white-space: nowrap; }
  .contact-list svg { width: 11px; height: 11px; margin-top: 4px; flex: none; }
  .contact-list .indent { padding-left: 18px; }

  /* Back */
  .card-back {
    background: var(--back-blue);
    color: var(--silver);
  }
  .back-content {
    position: absolute; inset: 0;
    display: flex; flex-direction: column; align-items: center; justify-content: center;
    gap: 10px;
  }
  .back-mark {
    font-size: 62px; font-weight: 600; letter-spacing: 1px; color: var(--silver);
    display: flex; align-items: center; gap: 14px;
  }
  .back-mark .dot {
    width: 20px; height: 20px; border-radius: 50%; background: var(--silver);
  }
  .back-company {
    font-size: 15px; letter-spacing: 1.5px; text-transform: uppercase;
  }
  .back-website { font-size: 15px; letter-spacing: 2px; }
</style>
</head>
<body>

<section class="card card-front">
  <div class="front-header">
    <div class="brand-lockup">
      <div class="brand-mark"><span class="dot"></span>Velmora</div>
      <div class="brand-divider"></div>
      <div class="brand-name">Velmora<br>Capital<br>Partners</div>
    </div>
    <div class="front-photo" role="img" aria-label="Aerial photograph of a city skyline with a glass office tower, trees and blue sky"></div>
  </div>
  <div class="front-band">
    <div class="person">
      <div class="person-name">Daniel Harcourt</div>
      <div class="person-title">CFA</div>
    </div>
    <ul class="contact-list">
      <li>
        <svg viewBox="0 0 24 24" fill="#fff"><path d="M6.6 10.8a15.1 15.1 0 0 0 6.6 6.6l2.2-2.2c.3-.3.7-.4 1-.2 1.1.4 2.3.6 3.6.6.6 0 1 .4 1 1V20c0 .6-.4 1-1 1A17 17 0 0 1 3 4c0-.6.4-1 1-1h3.5c.6 0 1 .4 1 1 0 1.3.2 2.5.6 3.6.1.3 0 .7-.2 1z"/></svg>
        555-014-2290
      </li>
      <li>
        <svg viewBox="0 0 24 24" fill="#fff"><path d="M2 5h20v14H2zM3.5 6.5 12 13l8.5-6.5z" fill-rule="evenodd"/></svg>
        info@velmoracapital.example
      </li>
      <li>
        <svg viewBox="0 0 24 24" fill="#fff"><path d="M12 2a7 7 0 0 0-7 7c0 5.2 7 13 7 13s7-7.8 7-13a7 7 0 0 0-7-7zm0 9.5A2.5 2.5 0 1 1 12 6.5a2.5 2.5 0 0 1 0 5z"/></svg>
        4820 Cedar Crest Blvd, Suite 610
      </li>
      <li class="indent">Riverton, TX 75000</li>
    </ul>
  </div>
</section>

<section class="card card-back">
  <div class="back-content">
    <div class="back-mark"><span class="dot"></span>Velmora</div>
    <div class="back-company">Velmora Capital Partners</div>
    <div class="back-website">www.velmoracapital.example</div>
  </div>
</section>

</body>
</html>
```